inspirational business card

I want to use the Vector on Pixmarra.com (number 61827405) and I will purchase the vector to send it to the designer once the general concept is approved. You can download it for free for a one time use on providing a design for this request.
Within the vector, insert:
Denise Halvorsen
Guidance and Cooperative

I prefer a vertical card but do not require vertical.

Contact info:

Denise Halvorsen, J.D.
Collaborative Lawyer
Certified Divorce Coach
Mediation Coach
PHONE 641/382-4076
EMAIL: dhrt@quelvo.net

Website: Guidanceandcooperative.com
Settlementcourse.com

I like greens, blue and grey. I do not want black font, and would like the font to be legible without needing perfect reading vision (no super small font).
I would like the overall theme to convey growth and nurturance.
I like the vector I selected because of the growth and light portrayed.
Not too frilly or too bold. I would like to to appeal to both sexes.

Target Market(s)

Generally professional women 35-60

Industry/Entity Type

Attorney

Font styles to use
Serif
Sans Serif

Colors
acd136
cadf82
fbf289
9d9d9d

Requirements
Must have
• My project does not need to have my photo but you could use it if you want
Nice to have
• Vertical
• I like rounded edges on the cards
Should not have
• I do not like my name appearing two times in close proximity. I'm not a flowery person.

```html
<!DOCTYPE html>
<html lang="en">
<head>
<meta charset="utf-8">
<title>Denise Halvorsen, J.D. – Business Card</title>
<link rel="stylesheet" href="https://fonts.googleapis.com/css2?family=Cormorant+Garamond:wght@500;600&family=Roboto+Condensed:wght@400;700&display=swap">
<style>
  :root {
    --stage: #e4e6e4;
    --card: #fbfbfa;
    --green: #8db33a;
    --green-light: #acd136;
    --green-pale: #cadf82;
    --grey: #7d7d7d;
    --grey-soft: #9d9d9d;
    --photo-dark: #1c1f24;
    --photo-mid: #4c5360;
  }
  * { box-sizing: border-box; margin: 0; padding: 0; }
  html, body { width: 1200px; height: 886px; overflow: hidden; }
  body {
    background: var(--stage);
    display: flex;
    align-items: center;
    justify-content: center;
    gap: 70px;
  }
  .card {
    border-radius: 22px;
    box-shadow: 0 10px 30px rgba(0,0,0,0.18);
    overflow: hidden;
    position: relative;
  }
  .card-back {
    width: 560px;
    height: 320px;
  }
  .portrait {
    position: absolute;
    inset: 0;
    background: radial-gradient(ellipse at 65% 40%, var(--photo-mid) 0%, var(--photo-dark) 75%);
  }
  .card-front {
    width: 320px;
    height: 560px;
    background: var(--card);
    color: var(--grey);
    font-family: "Roboto Condensed", sans-serif;
  }
  .foliage {
    position: absolute;
    right: 0;
    bottom: 0;
    width: 260px;
    height: 330px;
    background: radial-gradient(ellipse at 70% 55%, rgba(202,223,130,0.35) 0%, rgba(202,223,130,0.12) 55%, rgba(251,251,250,0) 80%);
  }
  .brand {
    position: absolute;
    top: 44px;
    left: 0;
    right: 0;
    text-align: center;
  }
  .brand-mark {
    display: block;
    margin: 0 auto 18px;
  }
  .brand-name {
    font-family: "Cormorant Garamond", serif;
    font-weight: 600;
    color: var(--grey);
    text-transform: uppercase;
    font-size: 21px;
    letter-spacing: 1px;
    line-height: 1.15;
  }
  .details {
    position: absolute;
    left: 40px;
    bottom: 40px;
    right: 24px;
  }
  .person-name {
    color: var(--green);
    font-weight: 700;
    font-size: 20px;
    text-transform: uppercase;
    letter-spacing: 0.3px;
  }
  .person-role { font-size: 16px; line-height: 1.3; }
  .contact { list-style: none; margin-top: 14px; font-size: 15px; line-height: 1.45; }
  .contact li { display: flex; align-items: center; gap: 8px; }
  .contact svg { flex: none; }
</style>
</head>
<body>
  <div class="card card-back">
    <div class="portrait" role="img" aria-label="Portrait photograph of the attorney in a dark blazer against a grey backdrop"></div>
  </div>

  <div class="card card-front">
    <div class="foliage" role="img" aria-label="Faint pale green tree illustration"></div>

    <div class="brand">
      <svg class="brand-mark" width="96" height="96" viewBox="0 0 96 96" aria-hidden="true">
        <circle cx="48" cy="48" r="44" fill="var(--green-light)"/>
      </svg>
      <p class="brand-name">Guidance and Cooperative</p>
    </div>

    <div class="details">
      <p class="person-name">Denise Halvorsen, J.D.</p>
      <p class="person-role">Collaborative Lawyer</p>
      <p class="person-role">Certified Divorce Coach</p>
      <p class="person-role">Mediation Coach</p>
      <ul class="contact">
        <li>
          <svg width="13" height="13" viewBox="0 0 24 24" aria-hidden="true"><path fill="var(--green)" d="M6.6 10.8a15.1 15.1 0 0 0 6.6 6.6l2.2-2.2a1 1 0 0 1 1-.25 11.4 11.4 0 0 0 3.6.57 1 1 0 0 1 1 1V20a1 1 0 0 1-1 1A17 17 0 0 1 3 4a1 1 0 0 1 1-1h3.5a1 1 0 0 1 1 1c0 1.25.2 2.45.57 3.6a1 1 0 0 1-.25 1z"/></svg>
          641/382-4076
        </li>
        <li>
          <svg width="13" height="13" viewBox="0 0 24 24" aria-hidden="true"><rect x="2" y="5" width="20" height="14" rx="2" fill="var(--green)"/><path d="M3 6l9 7 9-7" fill="none" stroke="#fff" stroke-width="1.8"/></svg>
          dhrt@quelvo.net
        </li>
        <li>
          <svg width="13" height="13" viewBox="0 0 24 24" aria-hidden="true"><circle cx="12" cy="12" r="10" fill="var(--green)"/><path d="M2 12h20M12 2c3 3 3 17 0 20M12 2c-3 3-3 17 0 20" fill="none" stroke="#fff" stroke-width="1.4"/></svg>
          Guidanceandcooperative.com
        </li>
        <li>
          <svg width="13" height="13" viewBox="0 0 24 24" aria-hidden="true"><circle cx="12" cy="12" r="10" fill="var(--green)"/><path d="M2 12h20M12 2c3 3 3 17 0 20M12 2c-3 3-3 17 0 20" fill="none" stroke="#fff" stroke-width="1.4"/></svg>
          Settlementcourse.com
        </li>
      </ul>
    </div>
  </div>
</body>
</html>
```